New finance and accounting services business needs banner ads

We need 3 web banner ads to use on local news websites. Our cool branding/logo (thank you Pixel Harbor!) will give you a great creative start to bring life to an otherwise dull service (that is the perception anyway).

Key ideas to be in the ads:
- We relieve stress for small business owners
- The cheapest way to get a CFO (Chief Financial Officer) is to 'rent' one part-time
- What will you do with all the cash we find you?

Target Market(s)

Small business owners (less than 50 employees) who are stressed out and don't like budgets, finance, or accounting

Industry/Entity Type

Professional Service

Other font styles liked:
• Fonts which match our logo

Colors

Designer to choose colors to be used in the design.

Requirements
Must have
• - Multiple sizes/layouts to fit within various ad spaces.
• - Show a message of stress relief
• - Show a message of the business owner getting more money (which helps with stress)
• - Must use the logo prominently (we are introducing the company with these ads)
Nice to have
• Some light-hearted humor is always a nice touch

```html
<!DOCTYPE html>
<html lang="en">
<head>
<meta charset="utf-8">
<title>Brightlane Ledger – Banner Set</title>
<link rel="stylesheet" href="https://fonts.googleapis.com/css2?family=Baloo+2:wght@800&family=Roboto+Condensed:wght@400;700&display=swap">
<style>
  :root {
    --stage: #26292d;
    --green: #2a9f2a;
    --green-dark: #1e861f;
    --green-light: #36b236;
    --sub-box: #1b7a1c;
    --yellow: #f6d63c;
    --white: #ffffff;
    --btn-top: #ffe27a;
    --btn-bottom: #f3a51c;
    --btn-text: #6a3a05;
    --btn-edge: #fff3c2;
    --art-top: #6b4a2a;
    --art-bottom: #f2ad3a;
  }
  * { box-sizing: border-box; margin: 0; padding: 0; }
  html, body { width: 1200px; height: 685px; overflow: hidden; }
  body { background: var(--stage); position: relative; font-family: "Roboto Condensed", sans-serif; }

  .banner { position: absolute; background: var(--green); overflow: hidden; }
  .banner > * { position: absolute; }
  .panel { inset: 0; width: 100%; height: 100%; }

  .brand { display: flex; flex-direction: column; align-items: center; color: var(--white); text-align: center; }
  .brand-mark { width: 34px; height: 34px; border-radius: 50%; background: var(--white); margin-bottom: 6px; }
  .brand-name { font-family: "Baloo 2", sans-serif; font-weight: 800; font-size: 14px; line-height: 1; letter-spacing: .3px; white-space: nowrap; }
  .brand-tag { font-size: 5px; letter-spacing: 1px; margin-top: 2px; border-top: 1px solid rgba(255,255,255,.5); padding-top: 1px; white-space: nowrap; }

  .headline { font-family: "Baloo 2", sans-serif; font-weight: 800; color: var(--yellow); text-align: center; line-height: .9; text-shadow: 0 2px 0 rgba(0,0,0,.18); white-space: nowrap; }
  .headline .big { display: block; }
  .subline { color: var(--yellow); text-align: center; line-height: 1; white-space: nowrap; }
  .subline.boxed { background: var(--sub-box); padding: 2px 6px; }

  .cta { display: flex; align-items: center; justify-content: center; border-radius: 6px; border: 2px solid var(--btn-edge);
         background: linear-gradient(var(--btn-top), var(--btn-bottom)); color: var(--btn-text);
         font-family: "Roboto Condensed", sans-serif; font-weight: 700; box-shadow: 0 2px 3px rgba(0,0,0,.3); white-space: nowrap; }

  .art { border-radius: 12px; background: linear-gradient(var(--art-top) 0%, var(--art-top) 45%, var(--art-bottom) 100%); }
</style>
</head>
<body>

<!-- Skyscraper wide -->
<section class="banner sky-wide" style="left:42px;top:24px;width:171px;height:641px;">
  <svg class="panel" viewBox="0 0 171 641" preserveAspectRatio="none"><polygon points="0,360 85,330 171,360 171,641 0,641" fill="var(--green-dark)"/></svg>
  <div class="brand" style="left:0;width:171px;top:20px;"><span class="brand-mark"></span><span class="brand-name">BRIGHTLANE LEDGER</span><span class="brand-tag">WE ARE FINANCE NERDS</span></div>
  <h2 class="headline" style="left:0;width:171px;top:196px;font-size:27px;">WHAT WILL<span class="big" style="font-size:37px;">YOU DO</span></h2>
  <p class="subline" style="left:0;width:171px;top:264px;font-size:16px;">WITH ALL THE CASH<br>WE FIND YOU?</p>
  <div class="art" role="img" aria-label="Cartoon finance nerd in a suit holding two bags of dollars" style="left:12px;top:310px;width:150px;height:262px;"></div>
  <a class="cta" style="left:33px;top:574px;width:106px;height:33px;font-size:15px;">LEARN MORE</a>
</section>

<!-- Skyscraper narrow -->
<section class="banner sky-narrow" style="left:231px;top:20px;width:129px;height:645px;">
  <svg class="panel" viewBox="0 0 129 645" preserveAspectRatio="none"><polygon points="0,330 64,300 129,330 129,645 0,645" fill="var(--green-dark)"/></svg>
  <div class="brand" style="left:0;width:129px;top:20px;"><span class="brand-mark"></span><span class="brand-name" style="font-size:12px;">BRIGHTLANE LEDGER</span><span class="brand-tag">WE ARE FINANCE NERDS</span></div>
  <h2 class="headline" style="left:0;width:129px;top:198px;font-size:22px;">WHAT WILL<span class="big" style="font-size:29px;">YOU DO</span></h2>
  <p class="subline" style="left:0;width:129px;top:248px;font-size:12.5px;">WITH ALL THE CASH<br>WE FIND YOU?</p>
  <div class="art" role="img" aria-label="Cartoon finance nerd in a suit holding two bags of dollars" style="left:6px;top:336px;width:117px;height:210px;"></div>
  <a class="cta" style="left:11px;top:578px;width:107px;height:33px;font-size:15px;">LEARN MORE</a>
</section>

<!-- Small leaderboard -->
<section class="banner board-small" style="left:382px;top:144px;width:522px;height:64px;">
  <svg class="panel" viewBox="0 0 522 64" preserveAspectRatio="none"><polygon points="0,0 120,0 140,32 120,64 0,64" fill="var(--green-dark)"/><polygon points="120,0 126,0 146,32 126,64 120,64 140,32" fill="var(--green-light)"/></svg>
  <div class="brand" style="left:0;width:120px;top:6px;"><span class="brand-mark" style="width:24px;height:24px;margin-bottom:4px;"></span><span class="brand-name" style="font-size:10px;">BRIGHTLANE LEDGER</span><span class="brand-tag" style="font-size:3.5px;">WE ARE FINANCE NERDS</span></div>
  <h2 class="headline" style="left:150px;width:266px;top:8px;font-size:27px;">WHAT WILL YOU DO</h2>
  <p class="subline boxed" style="left:160px;top:34px;font-size:16px;">WITH ALL THE CASH WE FIND YOU?</p>
  <a class="cta" style="left:440px;top:21px;width:72px;height:22px;font-size:10.5px;border-radius:4px;">LEARN MORE</a>
</section>

<!-- Large leaderboard -->
<section class="banner board-large" style="left:382px;top:232px;width:784px;height:96px;">
  <svg class="panel" viewBox="0 0 784 96" preserveAspectRatio="none"><polygon points="0,0 182,0 212,48 182,96 0,96" fill="var(--green-dark)"/><polygon points="182,0 192,0 222,48 192,96 182,96 212,48" fill="var(--green-light)"/></svg>
  <div class="brand" style="left:0;width:182px;top:6px;"><span class="brand-mark" style="width:40px;height:40px;"></span><span class="brand-name" style="font-size:15px;">BRIGHTLANE LEDGER</span><span class="brand-tag">WE ARE FINANCE NERDS</span></div>
  <h2 class="headline" style="left:230px;width:386px;top:14px;font-size:40px;">WHAT WILL YOU DO</h2>
  <p class="subline boxed" style="left:238px;top:51px;font-size:25px;">WITH ALL THE CASH WE FIND YOU?</p>
  <a class="cta" style="left:663px;top:30px;width:111px;height:34px;font-size:15px;">LEARN MORE</a>
</section>

<!-- Medium rectangle -->
<section class="banner rect-medium" style="left:382px;top:364px;width:362px;height:301px;">
  <svg class="panel" viewBox="0 0 362 301" preserveAspectRatio="none"><polygon points="188,0 362,0 362,301 188,301 214,150" fill="var(--green-light)"/><polygon points="198,0 362,0 362,301 198,301 224,150" fill="var(--green)"/></svg>
  <div class="brand" style="left:0;width:205px;top:14px;"><span class="brand-mark" style="width:40px;height:40px;"></span><span class="brand-name" style="font-size:15px;">BRIGHTLANE LEDGER</span><span class="brand-tag">WE ARE FINANCE NERDS</span></div>
  <h2 class="headline" style="left:0;width:205px;top:126px;font-size:31px;">WHAT WILL<span class="big" style="font-size:44px;">YOU DO</span></h2>
  <p class="subline boxed" style="left:20px;top:200px;font-size:13px;">WITH ALL THE CASH WE FIND YOU?</p>
  <a class="cta" style="left:65px;top:253px;width:86px;height:28px;font-size:13px;">LEARN MORE</a>
  <div class="art" role="img" aria-label="Cartoon finance nerd in a suit holding two bags of dollars" style="left:222px;top:62px;width:134px;height:236px;"></div>
</section>

<!-- Square -->
<section class="banner square" style="left:768px;top:396px;width:323px;height:269px;">
  <svg class="panel" viewBox="0 0 323 269" preserveAspectRatio="none"><polygon points="170,0 323,0 323,269 170,269 194,134" fill="var(--green-light)"/><polygon points="179,0 323,0 323,269 179,269 203,134" fill="var(--green)"/></svg>
  <div class="brand" style="left:0;width:180px;top:12px;"><span class="brand-mark" style="width:34px;height:34px;"></span><span class="brand-name" style="font-size:13px;">BRIGHTLANE LEDGER</span><span class="brand-tag">WE ARE FINANCE NERDS</span></div>
  <h2 class="headline" style="left:0;width:180px;top:116px;font-size:27px;">WHAT WILL<span class="big" style="font-size:38px;">YOU DO</span></h2>
  <p class="subline boxed" style="left:14px;top:180px;font-size:10.5px;">WITH ALL THE CASH WE FIND YOU?</p>
  <a class="cta" style="left:49px;top:229px;width:80px;height:24px;font-size:11.5px;">LEARN MORE</a>
  <div class="art" role="img" aria-label="Cartoon finance nerd in a suit holding two bags of dollars" style="left:198px;top:58px;width:120px;height:208px;"></div>
</section>

</body>
</html>
```